Sunny Paths and joy Business card

I have a logo, but will like a business card design. Is for a travel agency in Mexico. We focus in family experiences.

I will liek some thing different and unique, from the traditional business card, something to get remmeber for.

Business card information:

Leandro T. Ocampo
leandro@sunnypathsjoy.example

Alameda 482, 3 piso
Col. Tlalpizco
Mexico, D.F. 07320

office: (55) 5000-0142
mobile: (55) 9000-0187

www.sunnypathsjoy.example
@sunnypjoy
blog: sunnypathsandjoy.blogsite.example
facebook: SunnyPathsAndJoy

```html
<!DOCTYPE html>
<html lang="es">
<head>
<meta charset="utf-8">
<title>Sunny Paths and joy — Business card</title>
<link rel="stylesheet" href="https://fonts.googleapis.com/css2?family=Arimo:ital,wght@0,400;0,700;1,700&display=swap">
<style>
  :root {
    --brand-blue: #2a62b4;
    --brand-orange: #c2612a;
    --paper: #ffffff;
    --canvas: #ffffff;
    --ink-on-blue: #ffffff;
    --logo-ink: #1f4f9c;
  }
  * { box-sizing: border-box; margin: 0; padding: 0; }
  html, body {
    width: 1200px; height: 900px; overflow: hidden;
    background: var(--canvas);
    font-family: "Arimo", Arial, sans-serif;
  }
  .canvas { position: relative; width: 1200px; height: 900px; }
  .card {
    position: absolute; top: 54px;
    width: 430px; height: 810px;
    background: var(--paper);
    overflow: hidden;
    box-shadow: 4px 4px 8px rgba(0,0,0,0.25);
  }
  .card--front { left: 140px; }
  .card--back { left: 626px; }
  .card__art { position: absolute; inset: 0; width: 100%; height: 100%; display: block; }

  .brand-name {
    position: absolute; left: 0; right: 0; top: 324px;
    text-align: center;
    font-weight: 700; font-size: 38px; line-height: 1.1;
    color: var(--logo-ink);
  }
  .holder { position: absolute; left: 40px; top: 692px; color: var(--ink-on-blue); }
  .holder__name { font-weight: 700; font-style: italic; font-size: 19px; line-height: 26px; }
  .holder__email { font-size: 17px; line-height: 26px; }

  .contact {
    position: absolute; left: 44px; right: 20px;
    color: var(--ink-on-blue);
    font-size: 17px;
  }
  .contact--address { top: 432px; line-height: 28px; }
  .contact--phones { top: 538px; line-height: 28px; }
  .contact--online { top: 635px; line-height: 25px; }
  .contact__divider {
    position: absolute; left: 44px; right: 0; top: 611px;
    height: 3px; background: var(--ink-on-blue);
  }
</style>
</head>
<body>
<main class="canvas">

  <section class="card card--front" aria-label="Front of card">
    <svg class="card__art" viewBox="0 0 430 810" aria-hidden="true">
      <path d="M0,0 H430 V18 C300,36 130,80 0,150 Z" fill="var(--brand-blue)"/>
      <path d="M0,172 C130,104 300,58 430,40" fill="none" stroke="var(--brand-orange)" stroke-width="11"/>
      <path d="M0,194 C130,126 300,80 430,62" fill="none" stroke="var(--brand-orange)" stroke-width="3"/>
      <path d="M0,578 C140,542 300,536 430,566" fill="none" stroke="var(--brand-orange)" stroke-width="3"/>
      <path d="M0,606 C140,570 300,564 430,594" fill="none" stroke="var(--brand-orange)" stroke-width="11"/>
      <path d="M0,636 C140,600 300,594 430,624 V810 H0 Z" fill="var(--brand-blue)"/>
    </svg>
    <p class="brand-name">Sunny Paths<br>and joy</p>
    <div class="holder">
      <p class="holder__name">Leandro T. Ocampo</p>
      <p class="holder__email">leandro@sunnypathsjoy.example</p>
    </div>
  </section>

  <section class="card card--back" aria-label="Back of card">
    <svg class="card__art" viewBox="0 0 430 810" aria-hidden="true">
      <rect width="430" height="810" fill="var(--brand-blue)"/>
      <path d="M0,0 H430 V244 C300,256 150,280 0,316 Z" fill="var(--brand-orange)"/>
      <path d="M0,334 C150,298 300,272 430,258" fill="none" stroke="var(--paper)" stroke-width="3"/>
      <path d="M0,358 C150,322 300,296 430,282" fill="none" stroke="var(--paper)" stroke-width="3"/>
      <path d="M0,378 C150,344 300,318 430,304" fill="none" stroke="var(--paper)" stroke-width="2"/>
    </svg>
    <p class="contact contact--address">Alameda 482, 3 piso<br>Col. Tlalpizco<br>Mexico, D.F. 07320</p>
    <p class="contact contact--phones">office: (55) 5000-0142<br>mobile: (55) 9000-0187</p>
    <div class="contact__divider"></div>
    <p class="contact contact--online">www.sunnypathsjoy.example<br>@sunnypjoy<br>blog: sunnypathsandjoy.<br>blogsite.example<br>facebook: SunnyPathsAndJoy</p>
  </section>

</main>
</body>
</html>
```